Core Values Poster for Healthcare company

Trying to Create a core values poster for my company. Healthcare Company - We have Neurosurgery, Pain Management, Physical Therapy, Occupational Therapy, Rehab, Imaging, and psychology so far and we are growing fast.

Core Values would Include - (Execution), (Loyalty), (Innovation), (Synergy), (Growth-Oriented), (Ethics & Integrity), (Love), and (Energy)

Please incorporate the Company Logo which is on the website and I have included it in my uploads. As long as the logo stays blue it does not need a gradient effect.

I like the posters made for this contest : https://pinlarkstudio.com.au/flyer-work/briefs/build-team-ideals-flyer-580316

This picture should be memorable so people know our Core Values

Target Market(s)

Staff in the company

Colors

Designer to choose colors to be used in the design.

Requirements
Must have
• Logo
Nice to have
• Pictures for each core value

```html
<!DOCTYPE html>
<html lang="en">
<head>
<meta charset="utf-8">
<title>Clearview — Core Values</title>
<link rel="stylesheet" href="https://fonts.googleapis.com/css2?family=Cinzel:wght@700&family=Montserrat:wght@700&display=swap">
<style>
  :root {
    --paper: #f1f1f0;
    --navy: #0c3561;
    --brand-blue: #1c86c2;
    --heading: #f4f4f4;
    --label: #f6f6f6;
    --c-execution: #3b2216;
    --c-loyalty: #2db96d;
    --c-innovation: #e3158c;
    --c-synergy: #525254;
    --c-growth: #3ab54b;
    --c-ethics: #855634;
    --c-love: #772d9f;
    --c-energy: #ef901d;
  }
  * { margin: 0; padding: 0; box-sizing: border-box; }
  html, body { width: 900px; height: 1200px; overflow: hidden; }
  body { background: var(--paper); position: relative; font-family: "Montserrat", sans-serif; }

  .brand { position: absolute; top: 0; left: 30px; width: 842px; height: 137px; display: flex; align-items: center; justify-content: center; }
  .brand-name { font-family: "Montserrat", sans-serif; font-weight: 700; font-size: 60px; line-height: 1; color: var(--brand-blue); letter-spacing: 4px; }

  .panel { position: absolute; left: 30px; top: 137px; width: 842px; height: 1035px; background: var(--navy); }
  .panel-title { position: absolute; top: 38px; width: 100%; text-align: center; font-family: "Cinzel", serif; font-weight: 700; font-size: 50px; color: var(--heading); letter-spacing: -1px; }

  .value { position: absolute; left: 0; width: 842px; height: 107px; }
  .value-band { position: absolute; top: 27px; height: 53px; background: var(--c); display: flex; align-items: center; justify-content: center; color: var(--label); font-size: 25px; font-weight: 700; letter-spacing: 0.5px; white-space: nowrap; }
  .value-icon { position: absolute; top: 0; width: 196px; height: 107px; background: var(--c); border-radius: 9px; display: flex; align-items: center; justify-content: center; }
  .value-icon svg { width: 84px; height: 84px; fill: none; stroke: #fff; stroke-width: 2.4; stroke-linecap: round; stroke-linejoin: round; }

  .value--left .value-band { left: 0; width: 250px; }
  .value--left .value-icon { left: 250px; }
  .value--left.wide .value-band { width: 258px; }
  .value--left.wide .value-icon { left: 258px; }
  .value--right .value-icon { left: 416px; }
  .value--right .value-band { left: 612px; width: 230px; }
  .value-band.small { font-size: 21px; }
</style>
</head>
<body>
  <header class="brand">
    <div class="brand-name">CLEARVIEW</div>
  </header>

  <main class="panel">
    <h1 class="panel-title">CORE VALUES</h1>

    <section class="value value--left" style="--c: var(--c-execution); top: 119px;">
      <div class="value-band">Execution</div>
      <div class="value-icon">
        <svg viewBox="0 0 84 84" role="img" aria-label="Gears icon">
          <circle cx="34" cy="48" r="17" stroke-dasharray="5 4" stroke-width="6"/>
          <circle cx="34" cy="48" r="9"/>
          <circle cx="58" cy="24" r="11" stroke-dasharray="4 3.5" stroke-width="5"/>
          <circle cx="58" cy="24" r="5"/>
        </svg>
      </div>
    </section>

    <section class="value value--right" style="--c: var(--c-loyalty); top: 231px;">
      <div class="value-icon" role="img" aria-label="Loyalty icon: a figure holding a heart"></div>
      <div class="value-band">Loyalty</div>
    </section>

    <section class="value value--left wide" style="--c: var(--c-innovation); top: 345px;">
      <div class="value-band">Innovation</div>
      <div class="value-icon">
        <svg viewBox="0 0 84 84" role="img" aria-label="Lightbulb icon">
          <path d="M42 12a20 20 0 0 0-12 36c3 3 4 6 4 10h16c0-4 1-7 4-10a20 20 0 0 0-12-36z"/>
          <path d="M34 64h16M36 70h12"/>
          <path d="M42 12v46"/>
        </svg>
      </div>
    </section>

    <section class="value value--right" style="--c: var(--c-synergy); top: 457px;">
      <div class="value-icon">
        <svg viewBox="0 0 84 84" role="img" aria-label="Connected circle icon">
          <circle cx="42" cy="42" r="34"/>
          <circle cx="42" cy="42" r="24"/>
          <polygon points="42,30 53,38 49,51 35,51 31,38"/>
          <circle cx="42" cy="30" r="3"/><circle cx="53" cy="38" r="3"/><circle cx="49" cy="51" r="3"/><circle cx="35" cy="51" r="3"/><circle cx="31" cy="38" r="3"/>
        </svg>
      </div>
      <div class="value-band">Synergy</div>
    </section>

    <section class="value value--left wide" style="--c: var(--c-growth); top: 568px;">
      <div class="value-band small">Growth-Oriented</div>
      <div class="value-icon">
        <svg viewBox="0 0 84 84" role="img" aria-label="Rising bar chart icon">
          <rect x="6" y="58" width="10" height="20"/><rect x="20" y="56" width="10" height="22"/>
          <rect x="34" y="52" width="10" height="26"/><rect x="48" y="44" width="10" height="34"/>
          <rect x="62" y="32" width="10" height="46"/>
          <path d="M8 48C30 46 48 36 62 14"/><path d="M52 14h12v12"/>
        </svg>
      </div>
    </section>

    <section class="value value--right" style="--c: var(--c-ethics); top: 680px;">
      <div class="value-icon">
        <svg viewBox="0 0 84 84" role="img" aria-label="Balance scales icon">
          <path d="M42 8v60M14 18h56M28 78h28M34 68h16"/>
          <path d="M20 18l-10 22h20zM64 18l-10 22h20z"/>
          <path d="M10 40a10 6 0 0 0 20 0M54 40a10 6 0 0 0 20 0"/>
        </svg>
      </div>
      <div class="value-band small">Ethics &amp; Integrity</div>
    </section>

    <section class="value value--left wide" style="--c: var(--c-love); top: 794px;">
      <div class="value-band">Love</div>
      <div class="value-icon">
        <svg viewBox="0 0 84 84" role="img" aria-label="Two hearts icon">
          <path d="M30 66L10 44a12 12 0 0 1 20-14 12 12 0 0 1 20 14z"/>
          <path d="M50 74L32 54a11 11 0 0 1 18-13 11 11 0 0 1 18 13z"/>
        </svg>
      </div>
    </section>

    <section class="value value--right" style="--c: var(--c-energy); top: 907px;">
      <div class="value-icon">
        <svg viewBox="0 0 84 84" role="img" aria-label="Lightning bolt icon">
          <circle cx="42" cy="42" r="33"/>
          <path d="M48 12L28 46h14l-8 28 22-36H42z"/>
        </svg>
      </div>
      <div class="value-band">Energy</div>
    </section>
  </main>
</body>
</html>
```